Awesome Business Card Design needed!

Hey there.
I'm looking for a simple but awesome business card design.
Type of company: Online advertisement agency
(please don't use the typical business people or statistics images on the card)
The front has to display the business name
and possibly some sort of logo ( perhaps something with the two M's of the biz name )
And the back of the card should say:
Name
Phone
Email
Let your imagination flow.
here are some designs that I like and that you can use as inspiration.
Simple but Awesome
http://images.pixelvantor.net/designs/55128_877673_43091_thumbnail.jpg
http://images.pixelvantor.net/designs/37714_747642_40106_image.jpg
http://images.pixelvantor.net/designs/55128_877673_43091_image.jpg
http://images.pixelvantor.net/designs/51321_781878_43091_image.jpg
http://images.pixelvantor.net/designs/33378_399063_15912_image.jpg
http://images.pixelvantor.net/designs/2337_271604_9495_image.jpg
good luck

```html
<!DOCTYPE html>
<html lang="en">
<head>
<meta charset="utf-8">
<title>Velora Media – Business Card</title>
<link rel="stylesheet" href="https://fonts.googleapis.com/css2?family=Merriweather:wght@400&family=Roboto+Slab:wght@400;700&family=Varela+Round&display=swap">
<style>
  :root {
    --page-bg: #e9e9e9;
    --card-bg: #ffffff;
    --sky-blue: #4fb6e3;
    --sky-blue-edge: #3aa5d6;
    --ink-dark: #4a4a4a;
    --ink-body: #3c3c3c;
    --white: #ffffff;
  }
  html, body {
    margin: 0;
    padding: 0;
    width: 1200px;
    height: 900px;
    overflow: hidden;
    background: var(--page-bg);
  }
  .canvas {
    position: relative;
    width: 1200px;
    height: 900px;
  }
  .business-card {
    position: absolute;
    left: 120px;
    top: 176px;
    width: 960px;
    height: 548px;
    background: var(--card-bg);
    box-shadow: 0 6px 24px rgba(0,0,0,0.18);
    overflow: hidden;
  }
  .cloud-header {
    position: absolute;
    left: 0;
    top: 0;
    width: 500px;
    height: 200px;
  }
  .brand {
    position: absolute;
    left: 34px;
    top: 48px;
    display: flex;
    align-items: center;
    gap: 14px;
  }
  .brand-dot {
    width: 46px;
    height: 46px;
    border-radius: 50%;
    border: 4px solid var(--white);
    box-sizing: border-box;
  }
  .brand-name {
    font-family: "Varela Round", sans-serif;
    font-size: 46px;
    color: var(--white);
    line-height: 1;
  }
  .about-text {
    position: absolute;
    left: 36px;
    top: 200px;
    width: 420px;
    margin: 0;
    font-family: "Merriweather", serif;
    font-size: 10.5px;
    line-height: 1.55;
    color: var(--ink-body);
    text-align: justify;
  }
  .person {
    position: absolute;
    left: 555px;
    top: 208px;
  }
  .person-name {
    margin: 0;
    font-family: "Roboto Slab", serif;
    font-weight: 700;
    font-size: 40px;
    letter-spacing: 1px;
    color: var(--ink-dark);
    line-height: 1.05;
  }
  .person-role {
    margin: 4px 0 0;
    font-family: "Roboto Slab", serif;
    font-weight: 700;
    font-size: 22px;
    letter-spacing: 1px;
    color: var(--ink-dark);
  }
  .web-band {
    position: absolute;
    left: 0;
    top: 342px;
    width: 960px;
    height: 42px;
    background: var(--sky-blue);
    display: flex;
    align-items: center;
    justify-content: center;
    padding-left: 170px;
    box-sizing: border-box;
  }
  .web-address {
    font-family: "Varela Round", sans-serif;
    font-size: 28px;
    color: var(--white);
  }
  .contact-row {
    position: absolute;
    left: 315px;
    top: 428px;
    display: flex;
    align-items: center;
    gap: 70px;
    font-family: "Varela Round", sans-serif;
    font-size: 22px;
    color: var(--ink-dark);
  }
  .contact-item {
    display: flex;
    align-items: center;
    gap: 10px;
  }
  .contact-icon {
    display: block;
  }
</style>
</head>
<body>
<div class="canvas">
  <div class="business-card">
    <svg class="cloud-header" viewBox="0 0 500 200" aria-hidden="true">
      <path fill="var(--sky-blue)" stroke="var(--sky-blue-edge)" stroke-width="2"
        d="M0,0 H440 Q482,22 462,64 Q496,100 458,136 Q448,176 402,164 Q376,190 334,174 Q302,194 264,176 Q228,194 192,174 Q156,192 120,172 Q86,190 52,170 Q26,184 0,168 Z"/>
    </svg>
    <div class="brand">
      <span class="brand-dot"></span>
      <span class="brand-name">velora media</span>
    </div>

    <p class="about-text">We love our clients, and our clients love us, but we have to be sensitive to the idea that we simply cannot talk about what we are doing for someone. Trust us when we say that it can be frustrating to be so reserved sometimes. The work we do helps our clients reach people and grow their brands online every single day, and we are proud of it. Thanks for understanding, we know you will appreciate our discretion once you are a client too.</p>

    <div class="person">
      <h1 class="person-name">DANA REYES</h1>
      <p class="person-role">CONSULTANT</p>
    </div>

    <div class="web-band">
      <span class="web-address">www.veloramedia.com</span>
    </div>

    <div class="contact-row">
      <div class="contact-item">
        <svg class="contact-icon" width="30" height="22" viewBox="0 0 30 22" aria-hidden="true">
          <rect x="1.5" y="1.5" width="27" height="19" fill="none" stroke="var(--ink-dark)" stroke-width="2.5"/>
          <path d="M2 2 L15 12 L28 2" fill="none" stroke="var(--ink-dark)" stroke-width="2.5"/>
        </svg>
        <span>dreyes@veloramedia.com</span>
      </div>
      <div class="contact-item">
        <svg class="contact-icon" width="20" height="32" viewBox="0 0 20 32" aria-hidden="true">
          <rect x="2" y="2" width="16" height="28" rx="3" fill="none" stroke="var(--ink-dark)" stroke-width="2.5"/>
          <rect x="5" y="6" width="10" height="9" fill="var(--ink-dark)"/>
          <circle cx="10" cy="24" r="2" fill="var(--ink-dark)"/>
        </svg>
        <span>555.201.7734</span>
      </div>
    </div>
  </div>
</div>
</body>
</html>
```